Vehicle Rental Hire in the Algarve - Portugal

We are opening a Vehicle Rental company in the Algarve - Portugal - this will attract both locals and Tourists visiting. So we want this website to capture the beautiful location we will be set in, along with the familiarity of a vehicle rental company. And to keep a colour scheme in Line with out Logo. We are Marlenic Vehicle Rental.

Industry/Entity Type

Vehicle Rental

Number of Pages Required

1 page

Requirements
Must have
• must be professional, and simple to use navigation bar - must also have a "make a reservation" box - similar to the screenshot attached - Under our logo it must read "Vehicle Rental"
Nice to have
• It needs to be in a colour scheme that fits in with our logo

```html
<!DOCTYPE html>
<html lang="en">
<head>
<meta charset="utf-8">
<title>Marlenic Vehicle Rental</title>
<link href="https://fonts.googleapis.com/css2?family=Nunito+Sans:wght@400;600;700;800;900&display=swap" rel="stylesheet">
<style>
:root{
  --blue:#2a1fe0;
  --blue-deep:#1e17c9;
  --blue-soft:#3d35e8;
  --red:#d0302b;
  --ink:#111;
  --text:#444;
  --muted:#666;
  --white:#fff;
  --footer:#0b0b0b;
  --line:#e7e7ef;
}
*{box-sizing:border-box;margin:0;padding:0}
html,body{width:1200px;height:4267px;overflow:hidden}
body{font-family:"Nunito Sans",sans-serif;color:var(--ink);background:var(--white);position:relative}
.abs{position:absolute}
/* header */
.header{position:absolute;left:0;top:0;width:1200px;height:152px;background:var(--white)}
.logo-badge{position:absolute;left:128px;top:0;width:196px;height:180px;border-radius:0 0 98px 98px;background:var(--white);z-index:3;display:flex;align-items:center;justify-content:center}
.logo-ring{width:170px;height:170px;border:3px solid var(--blue);border-radius:50%;display:flex;flex-direction:column;align-items:center;justify-content:center;margin-top:10px}
.logo-name{font-weight:800;color:var(--blue);font-size:30px;letter-spacing:1px}
.logo-sub{font-weight:800;color:var(--blue);font-size:12px;letter-spacing:2px;margin-top:2px}
.follow{left:410px;top:50px;font-size:11px;color:#333;font-weight:600}
.social{display:flex;gap:7px;left:487px;top:43px}
.social span{width:24px;height:24px;border-radius:50%;background:var(--blue)}
.btn-call{left:642px;top:33px;width:259px;height:47px;border:2px solid var(--blue);border-radius:12px;color:var(--blue);font-size:15px;display:flex;align-items:center;justify-content:center;gap:10px}
.btn-book{left:925px;top:33px;width:140px;height:47px;background:var(--blue);border-radius:12px;color:#fff;font-size:15px;font-weight:700;display:flex;align-items:center;justify-content:center}
.nav{left:412px;top:106px;display:flex;gap:0;font-size:13px;font-weight:600;color:#222}
.nav a{color:inherit;text-decoration:none;position:absolute;white-space:nowrap}
.nav a.active{color:var(--blue);border-bottom:2px solid var(--blue);padding-bottom:6px}
/* hero */
.hero{left:0;top:152px;width:1200px;height:610px;background:linear-gradient(100deg,#1d7fb0 0%,#3ab0c4 22%,#d9c29a 48%,#e8d6b4 70%,#f1efe8 100%)}
.reserve{left:131px;top:198px;width:326px;height:522px;background:rgba(42,31,224,.82);border-radius:12px;padding:28px 27px;color:#fff}
.reserve h2{font-size:20px;font-weight:800;margin-bottom:14px}
.field-label{font-size:12px;margin:8px 0 6px}
.select{height:34px;background:#fff;border-radius:17px;color:#555;font-size:11px;display:flex;align-items:center;justify-content:space-between;padding:0 18px}
.row{display:flex;gap:12px}
.row .col{flex:1}
.btn-search{margin-top:22px;height:46px;border:2px solid #fff;background:var(--red);border-radius:23px;display:flex;align-items:center;justify-content:center;gap:8px;font-weight:800;font-size:16px}
.hero-title{left:537px;top:478px;color:#fff;font-size:36px;font-weight:900;line-height:48px;text-shadow:0 2px 6px rgba(0,0,0,.35)}
.hero-sub{left:538px;top:644px;color:#fff;font-size:15px;font-weight:800;text-shadow:0 1px 4px rgba(0,0,0,.4)}
/* welcome */
.welcome-h{left:132px;top:846px;font-size:26px;font-weight:800;line-height:38px}
.welcome-h span{color:var(--blue)}
.bar{height:4px;width:58px;background:var(--blue)}
.welcome-p{left:132px;top:983px;width:424px;font-size:14px;line-height:23px;color:var(--text);text-align:justify}
.btn-red{background:var(--red);color:#fff;border-radius:20px;font-weight:800;font-size:12.5px;display:flex;align-items:center;justify-content:center}
.welcome-photo{left:611px;top:826px;width:456px;height:464px;background:linear-gradient(180deg,#5d7c4f 0%,#9fae8f 40%,#c9cbc4 65%,#7e9a52 100%)}
.feature{width:222px;height:198px;background:#fff;border-radius:12px;box-shadow:0 6px 20px rgba(0,0,40,.08);text-align:center;padding-top:28px}
.feature h4,.svc h4{color:var(--blue);font-size:12.5px;font-weight:800;margin:16px 0 10px}
.feature p{font-size:11.5px;color:var(--muted);line-height:17px;padding:0 38px}
/* fleet */
.fleet{left:0;top:1558px;width:1200px;height:912px;background:linear-gradient(180deg,#4a4e55 0%,#5e5a52 30%,#3c3a39 100%)}
.sec-title{width:1200px;left:0;text-align:center;font-size:29px;font-weight:800}
.car{width:220px;height:344px;background:#fff;border-radius:8px;text-align:center}
.car .pic{margin:18px 16px 0;height:118px;border-radius:6px;background:linear-gradient(180deg,#f4f4f6,#dcdde2)}
.car h4{font-size:16px;font-weight:800;margin:28px 0 12px}
.car p{font-size:11.5px;color:var(--muted);line-height:17px;padding:0 30px}
.car .from{font-size:13px;color:#333;margin-top:18px}
.car .price{font-size:19px;color:var(--blue);font-weight:800;margin-top:6px}
.car .price small{font-size:13px;color:#333;font-weight:400}
/* extras */
.extras{left:0;top:2470px;width:1200px;height:863px;background:linear-gradient(180deg,#f4f5f9,#fbfbfd)}
.svc{width:296px;height:253px;background:#fff;border-radius:10px;box-shadow:0 6px 20px rgba(0,0,40,.07);text-align:center;padding-top:38px}
.svc p{font-size:12px;color:var(--muted);line-height:19px;padding:0 40px}
.scenery{left:0;top:3180px;width:1200px;height:153px;background:linear-gradient(90deg,#2a6f9a 0%,#8d8a6f 35%,#d9d2c6 60%,#c2485f 78%,#ebeae6 100%)}
/* testimonials */
.testi{left:0;top:3333px;width:1200px;height:557px;background:linear-gradient(180deg,#3a33e6,#2a22e0)}
.quote-card{width:284px;height:346px;background:#fff;border-radius:10px;padding:30px 38px}
.q{font-size:54px;font-weight:900;color:var(--blue);line-height:40px;height:42px}
.quote-card p{font-size:12.5px;color:#444;line-height:21px;margin-top:16px}
.quote-card .dash{width:36px;height:2px;background:#222;margin-top:36px}
.quote-card .who{font-size:12px;font-weight:700;margin-top:18px}
.arrow{width:34px;height:34px;border:2px solid #fff;border-radius:50%;display:flex;align-items:center;justify-content:center}
/* footer */
.footer{left:0;top:3890px;width:1200px;height:377px;background:var(--footer);color:#fff}
.f-logo{left:160px;top:50px;width:190px;height:190px;border:3px solid var(--blue);border-radius:50%;display:flex;flex-direction:column;align-items:center;justify-content:center}
.f-h{font-size:14px;font-weight:800}
.f-rule{height:2px;background:#fff;margin-top:10px}
.f-item{display:flex;gap:12px;align-items:flex-start;font-size:11.5px;line-height:15px;margin-top:16px}
.dot{width:22px;height:22px;border-radius:50%;background:var(--blue);flex:none}
.f-menu{font-size:11.5px;line-height:19px;margin-top:14px}
.copyright{left:0;width:1200px;top:332px;text-align:center;font-size:11px}
</style>
</head>
<body>

<header class="header">
  <div class="logo-badge"><div class="logo-ring"><div class="logo-name">MARLENIC</div><div class="logo-sub">VEHICLE RENTAL</div></div></div>
  <div class="abs follow">FOLLOW US</div>
  <div class="abs social"><span></span><span></span><span></span><span></span></div>
  <div class="abs btn-call">
    <svg width="18" height="18" viewBox="0 0 24 24" fill="none" stroke="currentColor" stroke-width="2"><path d="M5 3h4l2 5-3 2a12 12 0 0 0 6 6l2-3 5 2v4a2 2 0 0 1-2 2A17 17 0 0 1 3 5a2 2 0 0 1 2-2z"/></svg>
    CALL US +351 282 000 000</div>
  <div class="abs btn-book">BOOK NOW</div>
  <nav class="abs nav">
    <a class="active" style="left:0">HOME</a>
    <a style="left:73px">FLEET</a>
    <a style="left:150px">PROMOTIONS</a>
    <a style="left:273px">ABOUTUS</a>
    <a style="left:377px">SERVICES</a>
    <a style="left:481px">TARIFF</a>
    <a style="left:568px">CONTACT US</a>
  </nav>
</header>

<section>
  <div class="abs hero" role="img" aria-label="Algarve coastline with whitewashed town, cliffs, beach and turquoise sea"></div>
  <form class="abs reserve">
    <h2>MAKE A RESERVATION</h2>
    <div class="field-label">Pick up location</div>
    <div class="select">Please Choose <svg width="16" height="10" viewBox="0 0 16 10"><path d="M1 1l7 7 7-7" stroke="#2a1fe0" stroke-width="2" fill="none"/></svg></div>
    <div class="field-label" style="margin-top:16px">Driver's age</div>
    <div class="select">Please Choose <svg width="16" height="10" viewBox="0 0 16 10"><path d="M1 1l7 7 7-7" stroke="#2a1fe0" stroke-width="2" fill="none"/></svg></div>
    <div class="field-label" style="margin-top:16px">Vehicle category</div>
    <div class="select">Please Choose <svg width="16" height="10" viewBox="0 0 16 10"><path d="M1 1l7 7 7-7" stroke="#2a1fe0" stroke-width="2" fill="none"/></svg></div>
    <div class="row" style="margin-top:16px">
      <div class="col"><div class="field-label">Pick up date</div><div class="select">dd/mm/yyyy</div></div>
      <div class="col"><div class="field-label">Hour</div><div class="select">9:00 <svg width="16" height="10" viewBox="0 0 16 10"><path d="M1 1l7 7 7-7" stroke="#2a1fe0" stroke-width="2" fill="none"/></svg></div></div>
    </div>
    <div class="row" style="margin-top:10px">
      <div class="col"><div class="field-label">Drop off date</div><div class="select">dd/mm/yyyy</div></div>
      <div class="col"><div class="field-label">Hour</div><div class="select">9:00 <svg width="16" height="10" viewBox="0 0 16 10"><path d="M1 1l7 7 7-7" stroke="#2a1fe0" stroke-width="2" fill="none"/></svg></div></div>
    </div>
    <div class="btn-search"><svg width="18" height="18" viewBox="0 0 24 24" fill="none" stroke="#fff" stroke-width="2.4"><circle cx="10" cy="10" r="7"/><path d="M15 15l6 6"/></svg>SEARCH</div>
  </form>
  <h1 class="abs hero-title">HIGH QUALITY SERVICE<br>CAR HIRE IN ALGARVE,<br>PORTUGAL</h1>
  <div class="abs hero-sub">LOREM IPSUM IS SIMPLY DUMMY TEXT OF THE PRINTING</div>
</section>

<section>
  <h2 class="abs welcome-h">WELCOME TO<br><span>MARLENIC VEHICLE RENTAL</span></h2>
  <div class="abs bar" style="left:132px;top:940px"></div>
  <p class="abs welcome-p">Sed ut perspiciatis unde omnis iste natus error sit voluptatem accusantium doloremque laudantium, totam rem aperiam, eaque ipsa quae ab illo inventore veritatis et quasi architecto beatae vitae dicta sunt explicabo. Nemo enim ipsam voluptatem quia voluptas sit aspernatur aut odit aut fugit, sed quia consequuntur magni dolores eos qui ratione voluptatem sequi nesciunt. Neque porro quisquam est.</p>
  <div class="abs btn-red" style="left:131px;top:1178px;width:122px;height:40px">READ MORE</div>
  <div class="abs welcome-photo" role="img" aria-label="Family relaxing in the open boot of a white SUV in a pine forest"></div>

  <div class="abs feature" style="left:131px;top:1288px">
    <svg width="40" height="50" viewBox="0 0 40 50" fill="none" stroke="#2a1fe0" stroke-width="2"><circle cx="20" cy="18" r="14"/><path d="M25 12h-7a3 3 0 0 0 0 6h4a3 3 0 0 1 0 6h-7M20 8v4M20 24v4M20 32v14M14 42l6 6 6-6"/></svg>
    <h4>LOW PRICING</h4><p>Sed ut perspiciatis unde omnis iste natus error sit voluptatem accusa.</p></div>
  <div class="abs feature" style="left:373px;top:1288px">
    <svg width="44" height="50" viewBox="0 0 44 50" fill="none" stroke="#2a1fe0" stroke-width="2"><circle cx="22" cy="20" r="16"/><circle cx="22" cy="20" r="10"/><path d="M17 20l4 4 6-7M12 32l-4 14 6-3 4 5 3-12M32 32l4 14-6-3-4 5-3-12"/></svg>
    <h4>HIGH QUALITY</h4><p>Sed ut perspiciatis unde omnis iste natus error sit voluptatem accusa.</p></div>
  <div class="abs feature" style="left:611px;top:1288px">
    <svg width="46" height="50" viewBox="0 0 46 50" fill="none" stroke="#2a1fe0" stroke-width="2"><path d="M10 46V26h8l6-14c4 0 5 3 4 7l-2 7h12c3 0 4 3 3 5l-4 12c-1 2-2 3-4 3H18v-20M4 26h6v20H4zM34 4l2 4 4 2-4 2-2 4-2-4-4-2 4-2z"/></svg>
    <h4>CLEAN &amp; SAFE</h4><p>Sed ut perspiciatis unde omnis iste natus error sit voluptatem accusa.</p></div>
  <div class="abs feature" style="left:844px;top:1288px">
    <svg width="50" height="50" viewBox="0 0 50 50" fill="none" stroke="#2a1fe0" stroke-width="2"><path d="M25 3l5 4 6-1 2 6 6 3-1 6 4 5-4 5 1 6-6 3-2 6-6-1-5 4-5-4-6 1-2-6-6-3 1-6-4-5 4-5-1-6 6-3 2-6 6 1z"/><path d="M18 32l14-14"/><circle cx="19" cy="19" r="3"/><circle cx="31" cy="31" r="3"/></svg>
    <h4>BEST DISCOUNTS</h4><p>Sed ut perspiciatis unde omnis iste natus error sit voluptatem accusa.</p></div>
</section>

<section>
  <div class="abs fleet" role="img" aria-label="Rows of parked rental cars, darkened"></div>
  <h2 class="abs sec-title" style="top:1598px;color:#fff">OUR FLEET</h2>
  <div class="abs bar" style="left:571px;top:1660px;background:#fff"></div>

  <div class="abs car" style="left:132px;top:1716px"><div class="pic" role="img" aria-label="White crossover SUV"></div><h4>GROUP B1</h4><p>Sed ut perspiciatis unde omnis iste natus error sit voluptatem accusa.</p><div class="from">From</div><div class="price">7,35 € <small>/ Day</small></div></div>
  <div class="abs car" style="left:371px;top:1716px"><div class="pic" role="img" aria-label="Dark grey SUV"></div><h4>GROUP B2</h4><p>Sed ut perspiciatis unde omnis iste natus error sit voluptatem accusa.</p><div class="from">From</div><div class="price">7,35 € <small>/ Day</small></div></div>
  <div class="abs car" style="left:611px;top:1716px"><div class="pic" role="img" aria-label="Silver saloon car"></div><h4>GROUP C</h4><p>Sed ut perspiciatis unde omnis iste natus error sit voluptatem accusa.</p><div class="from">From</div><div class="price">7,35 € <small>/ Day</small></div></div>
  <div class="abs car" style="left:848px;top:1716px"><div class="pic" role="img" aria-label="Silver hatchback"></div><h4>GROUP D</h4><p>Sed ut perspiciatis unde omnis iste natus error sit voluptatem accusa.</p><div class="from">From</div><div class="price">7,35 € <small>/ Day</small></div></div>

  <div class="abs car" style="left:132px;top:2084px"><div class="pic" role="img" aria-label="White passenger van"></div><h4>GROUP B1</h4><p>Sed ut perspiciatis unde omnis iste natus error sit voluptatem accusa.</p><div class="from">From</div><div class="price">7,35 € <small>/ Day</small></div></div>
  <div class="abs car" style="left:371px;top:2084px"><div class="pic" role="img" aria-label="Blue SUV"></div><h4>GROUP B2</h4><p>Sed ut perspiciatis unde omnis iste natus error sit voluptatem accusa.</p><div class="from">From</div><div class="price">7,35 € <small>/ Day</small></div></div>
  <div class="abs car" style="left:611px;top:2084px"><div class="pic" role="img" aria-label="Silver compact saloon"></div><h4>GROUP C</h4><p>Sed ut perspiciatis unde omnis iste natus error sit voluptatem accusa.</p><div class="from">From</div><div class="price">7,35 € <small>/ Day</small></div></div>
  <div class="abs car" style="left:848px;top:2084px"><div class="pic" role="img" aria-label="Red city car"></div><h4>GROUP D</h4><p>Sed ut perspiciatis unde omnis iste natus error sit voluptatem accusa.</p><div class="from">From</div><div class="price">7,35 € <small>/ Day</small></div></div>
</section>

<section>
  <div class="abs extras"></div>
  <h2 class="abs sec-title" style="top:2522px;font-size:25px">EXTRAS &amp; SERVICES</h2>
  <div class="abs bar" style="left:571px;top:2582px"></div>
  <div class="abs scenery" role="img" aria-label="Algarve cliffs, sea and white houses with pink flowers"></div>

  <div class="abs svc" style="left:132px;top:2645px">
    <svg width="44" height="52" viewBox="0 0 44 52" fill="none" stroke="#2a1fe0" stroke-width="2"><rect x="6" y="2" width="26" height="48" rx="3"/><path d="M26 18a7 7 0 1 0-14 0c0 6 7 12 7 12s7-6 7-12z"/><circle cx="19" cy="18" r="2"/><path d="M10 44l10-8 12 6"/></svg>
    <h4>SAT-NAV - AUTO GREEN GPS</h4><p>Sed ut perspiciatis unde omnis iste natus error sit voluptatem accusa. Ut enim ad minima veniam.</p></div>
  <div class="abs svc" style="left:452px;top:2645px">
    <svg width="52" height="52" viewBox="0 0 52 52" fill="none" stroke="#2a1fe0" stroke-width="2"><rect x="6" y="4" width="16" height="12" rx="5"/><rect x="30" y="4" width="16" height="12" rx="5"/><path d="M4 20h20v26H4zM28 20h20v26H28zM8 30h12M32 30h12M8 38h12M32 38h12"/></svg>
    <h4>BABY SEAT</h4><p>Sed ut perspiciatis unde omnis iste natus error sit voluptatem accusa. Ut enim ad minima veniam.</p></div>
  <div class="abs svc" style="left:771px;top:2645px">
    <svg width="56" height="52" viewBox="0 0 56 52" fill="none" stroke="#2a1fe0" stroke-width="2"><rect x="8" y="4" width="40" height="8"/><path d="M12 12v36M12 20h36M22 34h24l-3-8H25zM20 34v10h28V34"/><circle cx="27" cy="40" r="2"/><circle cx="41" cy="40" r="2"/></svg>
    <h4>TRANSPONDER TOLL<br>ROAD - A22 (EX-SCUT)</h4><p>Sed ut perspiciatis unde omnis iste natus error sit voluptatem accusa. Ut enim ad minima veniam.</p></div>

  <div class="abs svc" style="left:132px;top:2923px">
    <svg width="56" height="50" viewBox="0 0 56 50" fill="none" stroke="#2a1fe0" stroke-width="2"><path d="M8 28l4-12h26l4 12M6 28h38v12H6zM10 40v6h6v-6M34 40v6h6v-6"/><circle cx="14" cy="34" r="2"/><circle cx="36" cy="34" r="2"/><path d="M46 4l2 4 4 2-4 2-2 4-2-4-4-2 4-2z"/></svg>
    <h4>TRAVEL ASSISTANCE</h4><p>Sed ut perspiciatis unde omnis iste natus error sit voluptatem accusa. Ut enim ad minima veniam.</p></div>
  <div class="abs svc" style="left:452px;top:2923px">
    <svg width="52" height="52" viewBox="0 0 52 52" fill="none" stroke="#2a1fe0" stroke-width="2"><path d="M14 18a12 12 0 0 1 24 0zM14 18h24v4a12 12 0 0 1-24 0zM6 50c2-10 10-16 20-16s18 6 20 16z"/><circle cx="26" cy="44" r="5"/></svg>
    <h4>ADDITIONAL DRIVER</h4><p>Sed ut perspiciatis unde omnis iste natus error sit voluptatem accusa. Ut enim ad minima veniam.</p></div>
  <div class="abs svc" style="left:771px;top:2923px">
    <svg width="52" height="52" viewBox="0 0 52 52" fill="none" stroke="#2a1fe0" stroke-width="2"><path d="M6 40l18-18 10 10-18 18zM24 22l8-8 10 10-8 8M40 12l8-6M36 8l4 4"/><path d="M18 36a4 4 0 1 1-1-5"/></svg>
    <h4>FUEL POLICY</h4><p>Sed ut perspiciatis unde omnis iste natus error sit voluptatem accusa. Ut enim ad minima veniam.</p></div>

  <div class="abs btn-red" style="left:522px;top:3232px;width:173px;height:38px;font-size:12px">VIEW ALL SERVICES</div>
</section>

<section>
  <div class="abs testi"></div>
  <h2 class="abs sec-title" style="top:3382px;color:#fff">TESTIMONIALS</h2>
  <div class="abs bar" style="left:585px;top:3443px;width:38px;background:#fff;height:3px"></div>
  <div class="abs arrow" style="left:59px;top:3643px"><svg width="14" height="14" viewBox="0 0 14 14" fill="none" stroke="#fff" stroke-width="2"><path d="M13 7H2M6 2L1 7l5 5"/></svg></div>
  <div class="abs arrow" style="left:1106px;top:3643px"><svg width="14" height="14" viewBox="0 0 14 14" fill="none" stroke="#fff" stroke-width="2"><path d="M1 7h11M8 2l5 5-5 5"/></svg></div>

  <div class="abs quote-card" style="left:132px;top:3494px"><div class="q">“</div><p>Sed ut perspiciatis unde omnis iste natus error sit voluptatem accusa ntium doloremque lauda ntium, totam rem aperiam, eaque ipsa quae ab illo inven tore verit atis et quasi architecto beatae vitae dicta sunt explic abo. Nemo enim ipsam voluptate.</p><div class="dash"></div><div class="who">RICHARD</div></div>
  <div class="abs quote-card" style="left:455px;top:3494px"><div class="q">“</div><p>Sed ut perspiciatis unde omnis iste natus error sit voluptatem accusa ntium doloremque lauda ntium, totam rem aperiam, eaque ipsa quae ab illo inven tore verit atis et quasi architecto beatae vitae dicta sunt explic abo. Nemo enim ipsam voluptate.</p><div class="dash"></div><div class="who">RICHARD</div></div>
  <div class="abs quote-card" style="left:782px;top:3494px"><div class="q">“</div><p>Sed ut perspiciatis unde omnis iste natus error sit voluptatem accusa ntium doloremque lauda ntium, totam rem aperiam, eaque ipsa quae ab illo inven tore verit atis et quasi architecto beatae vitae dicta sunt explic abo. Nemo enim ipsam voluptate.</p><div class="dash"></div><div class="who">RICHARD</div></div>
</section>

<footer class="abs footer">
  <div class="abs f-logo"><div class="logo-name" style="font-size:32px">MARLENIC</div><div class="logo-sub">VEHICLE RENTAL</div></div>
  <div class="abs" style="left:428px;top:62px;width:192px">
    <div class="f-h">CONTACT US</div><div class="f-rule"></div>
    <div class="f-item"><span class="dot"></span><span>12 Rua das Flores, 2nd Floor<br>Lagos, 8600-500</span></div>
    <div class="f-item"><span class="dot"></span><span>Call Us<br>+351 282 000 000</span></div>
    <div class="f-item"><span class="dot"></span><span>E mail Us<br>info@marlenicrental.com</span></div>
  </div>
  <div class="abs" style="left:750px;top:62px;width:106px">
    <div class="f-h">MENU</div><div class="f-rule"></div>
    <div class="f-menu">Home<br>Fleet<br>Promotions<br>AboutUs<br>Services<br>Tariff<br>Contact Us</div>
  </div>
  <div class="abs" style="left:963px;top:62px;width:106px">
    <div class="f-h">FOLLOW US</div><div class="f-rule"></div>
    <div class="f-item"><span class="dot"></span><span>Like us on<br>COMMUNITY</span></div>
    <div class="f-item"><span class="dot"></span><span>Follow us on<br>NETWORK</span></div>
    <div class="f-item"><span class="dot"></span><span>Follow us on<br>GALLERY</span></div>
  </div>
  <div class="abs" style="left:132px;top:290px;width:935px;height:1px;background:#555"></div>
  <div class="abs copyright">Copyright © 2024 All Rights Reserved</div>
</footer>

</body>
</html>
```